Business Card design for Founder and CEO of new shoe company

I am looking for a business card design for my new shoe company called Strido.

I am launching the company this April. Strido shoes offers slip-on athletic and casual style shoes for men and women. The unique selling point of the brand is that all of our shoe exist without shoelaces. I have included a link to the website to offer additional information about the company, see product images, and gain inspiration for the design. You can use the store owner password "Strido" to access the website.

www.Strido-shop.example

Thanks,
Dean Porlow

Target Market(s)

Active Men and Women ages 16-45

Industry/Entity Type

Business

Contact Information for Business Card

Dean Porlow
Founder and CEO
www.Strido-shop.example
deanporlow@Strido-shop.example
888-730-1964 / 888-7STRIDO
Strido, LLC
2384 N Tarrow St
Chicago, IL 60614

Requirements
Must have
• Be able to quickly and easily tell that Strido is a shoe company from the business card

```html
<!DOCTYPE html>
<html lang="en">
<head>
<meta charset="utf-8">
<title>Strido — Business Card</title>
<link href="https://fonts.googleapis.com/css2?family=Exo+2:wght@400&family=Open+Sans:wght@400&display=swap" rel="stylesheet">
<style>
  :root {
    --page-bg: #e9e6e1;
    --card-bg: #ffffff;
    --ink: #141414;
    --accent: #d94fae;
    --photo-pink: #d86ad0;
    --photo-blue: #5aa8dd;
    --photo-white: #f2f2f2;
  }
  * { margin: 0; padding: 0; box-sizing: border-box; }
  html, body {
    width: 1200px;
    height: 800px;
    overflow: hidden;
    background: var(--page-bg);
  }
  .stage {
    width: 1200px;
    height: 800px;
    display: flex;
    align-items: center;
    justify-content: center;
  }
  .business-card {
    width: 1050px;
    height: 600px;
    background: var(--card-bg);
    border-radius: 22px;
    box-shadow: 0 6px 24px rgba(0,0,0,0.12);
    display: flex;
    flex-direction: column;
    align-items: center;
    padding-top: 30px;
    text-align: center;
  }
  .brand-name {
    font-family: "Exo 2", sans-serif;
    font-weight: 400;
    font-size: 64px;
    letter-spacing: 3px;
    color: var(--ink);
    display: flex;
    align-items: center;
    gap: 22px;
    line-height: 1;
  }
  .brand-mark {
    width: 40px;
    height: 40px;
    border-radius: 50%;
    background: var(--ink);
  }
  .holder-name {
    font-family: "Open Sans", sans-serif;
    font-size: 34px;
    color: var(--accent);
    margin-top: 34px;
    line-height: 1.1;
  }
  .holder-title {
    font-family: "Open Sans", sans-serif;
    font-size: 21px;
    color: var(--ink);
    margin-top: 8px;
  }
  .product-photo {
    width: 730px;
    height: 150px;
    margin-top: 22px;
    border-radius: 6px;
    background: linear-gradient(90deg,
      var(--photo-pink) 0%, var(--photo-blue) 30%,
      var(--photo-white) 42%, var(--photo-white) 58%,
      var(--photo-blue) 72%, #8cc8ee 100%);
    opacity: 0.85;
  }
  .contact-list {
    list-style: none;
    margin-top: 30px;
    font-family: "Open Sans", sans-serif;
    font-size: 25px;
    color: var(--accent);
    line-height: 1.45;
  }
</style>
</head>
<body>
  <main class="stage">
    <section class="business-card">
      <h1 class="brand-name"><span class="brand-mark"></span>Strido</h1>
      <p class="holder-name">Dean Porlow</p>
      <p class="holder-title">Founder and CEO</p>
      <div class="product-photo" role="img" aria-label="Product photo: pink and blue slip-on sneakers, a white cap and light blue slip-on sneakers on white"></div>
      <ul class="contact-list">
        <li>888-730-1964</li>
        <li>www.Strido-shop.example</li>
        <li>deanporlow@Strido-shop.example</li>
        <li>Strido, LLC&nbsp;&nbsp;2384 N Tarrow St Chicago, IL 60614</li>
      </ul>
    </section>
  </main>
</body>
</html>
```